Customer Value Leaflet

We need a bi-fold brochure designing, based on the attached PDF wireframes. Our company name is quillbrookery.com (of which the logo is currently being designed). The corporate colour is orange (the exact shade of which we are happy to leave to the designers discretion).

The leaflet will distributed to customer experience experts and marketers so the design needs to be bright, engaging, clean and simple. Design is critical.

```html
<!DOCTYPE html>
<html lang="en">
<head>
<meta charset="utf-8">
<title>Customer Value Leaflet – quillbrookery.com</title>
<link rel="stylesheet" href="https://fonts.googleapis.com/css2?family=Open+Sans:wght@400;600;700;800&display=swap">
<style>
:root{
  --pink:#e0157a;
  --blue:#0d7fc8;
  --blue-dark:#0a5f9a;
  --orange:#f39422;
  --red:#c8102e;
  --ink:#111111;
  --grey:#555555;
  --grey-light:#8a8a8a;
  --page-top:#ffffff;
  --page-bottom:#e6e6e6;
  --white:#ffffff;
}
*{margin:0;padding:0;box-sizing:border-box}
html,body{width:1200px;height:3396px;overflow:hidden}
body{font-family:"Open Sans",Arial,sans-serif;background:linear-gradient(180deg,var(--page-top) 0%,#f3f3f3 40%,var(--page-bottom) 100%);position:relative;color:var(--ink)}
.abs{position:absolute}
.portrait{top:0;height:600px;width:600px}
.portrait--kim{left:0;background:linear-gradient(160deg,#f7f7f7 0%,#e9e6e3 45%,#c9b3a2 100%)}
.portrait--kevin{left:600px;background:linear-gradient(200deg,#f4f4f4 0%,#dfe0e2 50%,#b8b2ab 100%)}
.intro{top:600px;height:255px;border-radius:0 0 22px 22px;color:var(--white);text-align:center;padding-top:20px}
.intro--kim{left:40px;width:523px;background:var(--pink)}
.intro--kevin{left:651px;width:501px;background:linear-gradient(180deg,var(--blue),var(--blue-dark))}
.intro__title{font-size:48px;font-weight:700;letter-spacing:-1px;line-height:1.15}
.intro__text{font-size:24px;line-height:37px;margin-top:6px;padding:0 10px}
.lead{top:882px;left:0;width:1200px;text-align:center;font-size:50px;color:var(--grey);line-height:62px}
.site{top:1028px;left:0;width:1200px;text-align:center;font-size:52px;font-weight:700;letter-spacing:-1px;line-height:72px}
.timeline{top:1160px;left:598px;width:4px;height:950px;background:#d9d9d9}
.stage{left:475px;width:250px;height:42px;border-radius:21px 21px 0 0;background:var(--orange);color:var(--white);font-size:28px;font-weight:700;text-align:center;line-height:42px}
.card{height:230px;border-radius:22px;color:var(--white);text-align:center;padding-top:16px}
.card--kim{left:82px;width:507px;background:var(--pink)}
.card--kevin{left:614px;width:493px;background:linear-gradient(180deg,var(--blue),var(--blue-dark))}
.card__text{font-size:27px;line-height:1.15;padding:0 10px}
.card__text small{font-size:20px;display:block}
.card__icon{display:block;margin:10px auto 0}
.brand-mark{display:inline-flex;align-items:center;gap:12px;margin-top:22px;font-size:34px;font-weight:700;color:var(--white)}
.brand-mark__dot{width:28px;height:28px;border-radius:50%;background:var(--white)}
.verdict-avatar{left:334px;top:2113px;width:130px;height:130px;border-radius:50%;border:6px solid #d0d0d0;background:linear-gradient(160deg,#eeeeee,#b9b2aa)}
.verdict{left:458px;top:2142px;width:453px;height:74px;border-radius:37px;background:var(--red);color:var(--white);font-size:44px;line-height:74px;padding-left:30px;white-space:nowrap}
.pitch{left:0;width:1200px;text-align:center;white-space:nowrap}
.pitch--lead{top:2282px;font-size:48px;font-weight:600;line-height:66px}
.pitch--headline{top:2341px;font-size:66px;font-weight:700;color:var(--red);letter-spacing:-1px;line-height:90px}
.pitch--sub{top:2412px;font-size:40px;font-weight:600;line-height:56px}
.pitch--find{top:2468px;font-size:50px;font-weight:700;color:#333;line-height:70px}
.url-pill{left:222px;top:2541px;width:756px;height:86px;border-radius:43px;background:var(--red);color:var(--white);font-size:56px;font-weight:700;text-align:center;line-height:86px;white-space:nowrap}
.platform{left:150px;top:2650px;width:900px;text-align:center}
.platform__title{font-size:31px;font-weight:700;color:#333;line-height:37px}
.platform__text{font-size:28px;color:var(--grey-light);line-height:34px;margin-top:12px}
.sign-holder{left:283px;top:2900px;width:651px;height:496px;background:linear-gradient(180deg,#f7f7f7 0%,#efe9e5 55%,#c43a3a 100%)}
</style>
</head>
<body>
<div class="abs portrait portrait--kim" role="img" aria-label="Photo of a smiling woman in a white shirt working at a laptop"></div>
<div class="abs portrait portrait--kevin" role="img" aria-label="Photo of a thoughtful man in a white shirt at a laptop"></div>

<div class="abs intro intro--kim">
  <div class="intro__title">MEET KIM</div>
  <p class="intro__text">Kim has purchased<br>3 items from you over the past 3 months<br>@ £109 margin and you acquired her<br>though a Searchly PPC campaign</p>
</div>
<div class="abs intro intro--kevin">
  <div class="intro__title">MEET KEVIN</div>
  <p class="intro__text">Kevin purchased<br>an item last week @ £31 margin and<br>you acquired him though a retarget-<br>ing campaign</p>
</div>

<p class="abs lead">Right now you probably think<br>Kim is your best customer…</p>
<p class="abs site">www.quillbrookery.com</p>

<div class="abs timeline"></div>

<div class="abs stage" style="top:1175px">+ 1 WEEK</div>
<div class="abs card card--kim" style="top:1217px">
  <p class="card__text">Kim calls you to return<br>an item…</p>
  <svg class="card__icon" width="110" height="110" viewBox="0 0 110 110" fill="none" stroke="#fff" stroke-width="8" stroke-linecap="round">
    <path d="M22 62V50a33 33 0 0 1 66 0v12"/>
    <rect x="14" y="56" width="16" height="26" rx="6" fill="#fff"/>
    <rect x="80" y="56" width="16" height="26" rx="6" fill="#fff"/>
    <path d="M88 82q0 16-24 16"/>
    <circle cx="58" cy="98" r="5" fill="#fff"/>
  </svg>
</div>
<div class="abs card card--kevin" style="top:1217px">
  <p class="card__text">Kevin makes  another<br>purchase…</p>
  <svg class="card__icon" width="120" height="120" viewBox="0 0 120 120" fill="#fff">
    <rect x="52" y="6" width="16" height="30"/>
    <path d="M38 34h44L60 58z"/>
    <rect x="10" y="64" width="100" height="14"/>
    <path d="M18 80h84l-8 34H26z"/>
    <rect x="36" y="86" width="8" height="22" fill="#0b6aab"/><rect x="56" y="86" width="8" height="22" fill="#0b6aab"/><rect x="76" y="86" width="8" height="22" fill="#0b6aab"/>
  </svg>
</div>

<div class="abs stage" style="top:1495px">+ 1 MONTH</div>
<div class="abs card card--kim" style="top:1537px">
  <p class="card__text">Places 4 more online orders…</p>
  <svg class="card__icon" width="130" height="130" viewBox="0 0 130 130" fill="none" stroke="#fff" stroke-width="9" stroke-linejoin="round">
    <path d="M6 20h18l14 72h70l12-54H32"/>
    <path d="M54 62l14 14 26-28" stroke-linecap="round"/>
    <circle cx="48" cy="114" r="8" fill="#fff"/><circle cx="100" cy="114" r="8" fill="#fff"/>
  </svg>
</div>
<div class="abs card card--kevin" style="top:1537px">
  <p class="card__text">Then 2 more<small>(and even tweets about<br>how great your service is)…</small></p>
  <div class="brand-mark"><span class="brand-mark__dot"></span>Chirper</div>
</div>

<div class="abs stage" style="top:1806px">+ 6 MONTHS</div>
<div class="abs card card--kim" style="top:1848px">
  <p class="card__text">Then places another<br>order but doesn't come<br>back for a month</p>
  <svg class="card__icon" width="96" height="96" viewBox="0 0 100 100">
    <path d="M30 4h40l26 26v40L70 96H30L4 70V30z" fill="#fff"/>
    <path d="M34 34l32 32M66 34L34 66" stroke="#e0157a" stroke-width="12" stroke-linecap="round"/>
  </svg>
</div>
<div class="abs card card--kevin" style="top:1848px">
  <p class="card__text">And continues to make<br>purchases on a bi-monthly basis</p>
  <svg class="card__icon" width="120" height="120" viewBox="0 0 130 130" fill="none" stroke="#fff" stroke-width="9" stroke-linejoin="round">
    <path d="M6 20h18l14 72h70l12-54H32"/>
    <path d="M54 62l14 14 26-28" stroke-linecap="round"/>
    <circle cx="48" cy="114" r="8" fill="#fff"/><circle cx="100" cy="114" r="8" fill="#fff"/>
  </svg>
</div>

<div class="abs verdict">but really it is Kevin.</div>
<div class="abs verdict-avatar" role="img" aria-label="Small round portrait of Kevin"></div>

<p class="abs pitch pitch--lead">By predicting</p>
<p class="abs pitch pitch--headline">Customer Lifetime Valuetoday…</p>
<p class="abs pitch pitch--sub">…you can optimise your business for tomorrow</p>
<p class="abs pitch pitch--find">Find our more at</p>
<div class="abs url-pill">www.quillbrookery.com</div>

<div class="abs platform">
  <p class="platform__title">Veyra is our Customer Value Platform,<br>designed for Marketers in the Digital Enterprise.</p>
  <p class="platform__text">Veyra is like having a team of data<br>scientistsmaking valuable insights available<br>to your website in real-time so you can deliver<br>the ultimate customer experience.</p>
</div>

<div class="abs sign-holder" role="img" aria-label="Photo of a person in red holding up a white card with a drawn smiley"></div>
</body>
</html>
```